Online interactive tutorial for year 2 to year 12 students in Australia

Website design for a new Brightlane Tutoring for year 2 to year 12 students in Australia.

- The tutorial will be conducted via live webcam and within a dedicated interactive space
- The tutorial will be provided by high scoring undergraduates studying in top Australian universities.
- The tutors will be going through interviews & assessments & only top students are allowed to apply.
- Parents will do search and select tutor and have short 15 mins video interaction with potential tutors before booking them for their children for tutoring.
- hourly cost of booking (no monthly subscription or no hour limits)
- Tutors will have their own profile

Please see the attached for detailed page functionality.

The look and feel of the design must consider the following:
- must be educational but not dull and should stand out
- must appeal to younger generation - tutees (8-18 years), tutors (19-25), parents (30-50).
- Ideas for Logos (brivano.com.au but not confirmed)

Target Market(s)

tutees (8-18 years), tutors (19-25 years), parents (30-50 years).

Industry/Entity Type

Education

Coding

Coded - Design and coding required

Number of Pages Required

5+ page

Font styles to use
Serif

Requirements
Must have
• The look and feel of the design must consider the following:
• - must be educational but not dull and should stand out
• - must appeal to younger generation - tutees (8-18 years), tutors (19-25), parents (30-50).
Should not have
• Dullness

```html
<!DOCTYPE html>
<html lang="en">
<head>
<meta charset="utf-8">
<title>Brightlane Tutoring</title>
<link rel="stylesheet" href="https://fonts.googleapis.com/css2?family=Playfair+Display:wght@700;900&family=Montserrat:wght@400;600;700&family=Lora:ital,wght@0,400;0,700;1,400&display=swap">
<style>
:root{
  --brown:#3e2a1e;
  --brown-dark:#2f1f16;
  --mint:#6cc3a1;
  --mint-dark:#58b08e;
  --ink:#222;
  --muted:#888;
  --line:#e4e4e4;
  --grey-bg:#f3f3f3;
  --white:#fff;
}
*{box-sizing:border-box;margin:0;padding:0}
html,body{width:1200px;height:3838px;overflow:hidden}
body{font-family:"Lora",Georgia,serif;color:var(--ink);background:var(--white);position:relative}

/* top bar */
.topbar{position:absolute;left:0;top:0;width:1200px;height:31px;background:var(--brown-dark);color:#fff;font:600 10px "Montserrat",sans-serif}
.topbar .lang{position:absolute;left:130px;top:10px;display:flex;align-items:center;gap:6px}
.topbar .lang i{width:10px;height:10px;border-radius:50%;border:1px solid #fff;display:block}
.topbar .social{position:absolute;left:274px;top:10px;display:flex;gap:12px}
.topbar .social i{width:10px;height:10px;border-radius:50%;background:#cbbfb6;display:block}
.topbar .login{position:absolute;left:914px;top:4px;width:70px;height:23px;border-radius:12px;background:var(--mint);text-align:center;line-height:23px}
.topbar .register{position:absolute;left:990px;top:4px;width:80px;height:23px;border-radius:12px;border:1px solid #8a7b70;text-align:center;line-height:21px}

/* header */
.header{position:absolute;left:0;top:31px;width:1200px;height:92px;background:#fff}
.brand{position:absolute;left:130px;top:32px;display:flex;align-items:center;gap:10px;font:700 20px "Montserrat",sans-serif;color:var(--brown)}
.brand i{width:22px;height:22px;border-radius:50%;background:var(--mint);display:block}
.nav{position:absolute;left:462px;top:38px;display:flex;font:700 11px "Montserrat",sans-serif;color:var(--ink)}
.nav a{color:inherit;text-decoration:none;margin-right:25px;padding-bottom:6px}
.nav a.active{border-bottom:2px solid var(--mint)}

/* hero */
.hero{position:absolute;left:0;top:123px;width:1200px;height:535px;background:linear-gradient(110deg,#6b5a4e 0%,#c9b39b 30%,#e8e2d6 55%,#9fb3a8 80%,#d7dcd6 100%)}
.hero-card{position:absolute;left:264px;top:445px;width:675px;height:90px;background:#fff;display:flex}
.hero-card .tag{width:40px;background:var(--brown);color:#fff;font:700 9px "Montserrat",sans-serif;writing-mode:vertical-rl;transform:rotate(180deg);text-align:center;letter-spacing:1px}
.hero-card .body{padding:13px 18px;width:440px}
.hero-card h2{font:700 17px "Montserrat",sans-serif;margin-bottom:7px}
.hero-card p{font-size:11px;color:#555;line-height:1.5}
.btn-pill{display:inline-block;background:var(--mint);color:#fff;font:700 11px "Montserrat",sans-serif;border-radius:22px;text-align:center}
.hero-card .btn-pill{position:absolute;right:30px;top:27px;width:152px;height:42px;line-height:42px}

/* section titles */
.sec-title{position:absolute;left:0;width:1200px;text-align:center}
.sec-title h2{font:900 38px "Playfair Display",serif}
.sec-title span{display:block;font:600 9px "Montserrat",sans-serif;letter-spacing:2px;color:var(--muted);margin-top:2px;text-transform:uppercase}
.sec-title svg{display:block;margin:6px auto 0}

/* events */
.events{position:absolute;left:0;top:658px;width:1200px;height:596px;background:var(--brown);color:#fff}
.events .sec-title span{color:#cfc3b9}
.event{position:absolute;top:174px;width:458px;height:325px;background:#fff;color:var(--ink)}
.event .date{position:absolute;left:0;top:0;width:82px;height:85px;background:var(--mint);color:#fff;text-align:center;font-family:"Montserrat",sans-serif}
.event .date b{display:block;font-size:28px;padding-top:14px}
.event .date small{font-size:9px;font-weight:700}
.event .meta{position:absolute;left:100px;top:20px;font:400 10px "Montserrat",sans-serif;color:var(--muted)}
.event h3{position:absolute;left:100px;top:40px;font:700 15px "Montserrat",sans-serif}
.event .img{position:absolute;left:0;top:85px;width:458px;height:240px}

/* news */
.news{position:absolute;left:0;top:1254px;width:1200px;height:614px;background:#fff}
.post{position:absolute;top:169px;width:297px}
.post .img{height:177px}
.post .meta{font:400 9px "Montserrat",sans-serif;color:var(--muted);margin-top:15px}
.post h3{font:700 14px "Montserrat",sans-serif;margin-top:9px}
.post p{font-size:11px;color:#777;line-height:1.65;margin-top:10px}
.post .more{display:block;font:700 9px "Montserrat",sans-serif;color:var(--mint);letter-spacing:1px;margin-top:14px}

/* teachers */
.teachers{position:absolute;left:0;top:1868px;width:1200px;height:435px;background:var(--grey-bg)}
.teacher{position:absolute;top:169px;width:136px;text-align:center}
.teacher .img{height:138px}
.teacher h4{font:700 10px "Montserrat",sans-serif;margin-top:18px}
.teacher small{display:block;font-size:9px;color:var(--muted);margin-top:6px}

/* courses */
.courses{position:absolute;left:0;top:2303px;width:1200px;height:965px;background:#fff}
.course{position:absolute;background:#fff;border:1px solid var(--line);text-align:center}
.course .img{position:absolute;left:0;top:0;width:100%}
.course .price{position:absolute;left:50%;width:60px;height:60px;margin-left:-30px;border-radius:50%;background:var(--mint);color:#fff;font:700 12px "Montserrat",sans-serif;line-height:54px;border:3px solid #fff}
.course p{position:absolute;left:0;width:100%;font:italic 10px "Lora",serif;color:#666}
.course h4{position:absolute;left:0;width:100%;font:700 13px "Montserrat",sans-serif}
.view-all{position:absolute;left:0;top:896px;width:1200px;text-align:center;font:700 9px "Montserrat",sans-serif;letter-spacing:1.5px;color:var(--mint)}

/* cta */
.cta{position:absolute;left:0;top:3268px;width:1200px;height:192px;background:var(--mint);color:#fff;text-align:center}
.cta h2{font:700 26px "Montserrat",sans-serif;margin-top:44px}
.cta p{font:700 11px "Montserrat",sans-serif;margin-top:8px;letter-spacing:.5px}
.cta .btn{display:inline-block;margin-top:20px;background:#fff;color:var(--ink);font:700 11px "Montserrat",sans-serif;border-radius:22px;width:192px;height:40px;line-height:40px}

/* footer */
.footer{position:absolute;left:0;top:3460px;width:1200px;height:327px;background:var(--brown);color:#fff}
.fcol{position:absolute;top:50px;width:210px}
.fcol h5{font:700 14px "Playfair Display",serif;padding-bottom:12px;border-bottom:1px solid #5c4638;margin-bottom:14px}
.fcol p{font-size:11px;color:#cfc3b9;line-height:1.65}
.fcol .email{margin-top:18px;height:34px;border:1px solid #6a5446;border-radius:18px;font:700 9px "Montserrat",sans-serif;padding:0 14px;line-height:32px;display:flex;justify-content:space-between}
.fpost{margin-bottom:16px;padding-bottom:14px;border-bottom:1px solid #5c4638}
.fpost b{display:block;font:700 11px "Montserrat",sans-serif}
.fpost small{font-size:10px;color:#cfc3b9}
.flinks li{list-style:none;font:400 11px "Montserrat",sans-serif;color:#e6ddd5;margin-bottom:14px}
.contact-line{font:700 13px "Montserrat",sans-serif;margin:12px 0 10px}
.fsocial{display:flex;gap:8px;margin-top:14px}
.fsocial i{width:24px;height:24px;border-radius:50%;border:1px solid #8a7b70;display:block}
.copyright{position:absolute;left:0;top:3787px;width:1200px;height:51px;background:var(--brown-dark);color:#cfc3b9;text-align:center;font:400 10px "Montserrat",sans-serif;line-height:51px}
</style>
</head>
<body>

<div class="topbar">
  <div class="lang"><i></i>Choose your language</div>
  <div class="social"><i></i><i></i><i></i><i></i><i></i><i></i><i></i></div>
  <div class="login">Login</div>
  <div class="register">Register</div>
</div>

<header class="header">
  <div class="brand"><i></i>Brightlane Tutoring</div>
  <nav class="nav">
    <a class="active">HOME</a><a>ABOUT US</a><a>EVENTS</a><a>REGISTRATION</a><a>STUDENT</a><a>TUTOR</a><a>SCHEDULE</a><a>CONTACT US</a>
    <svg width="12" height="12" viewBox="0 0 12 12"><circle cx="5" cy="5" r="3.8" fill="none" stroke="#222" stroke-width="1.6"/><line x1="8" y1="8" x2="11" y2="11" stroke="#222" stroke-width="1.6"/></svg>
  </nav>
</header>

<section class="hero" role="img" aria-label="Photo of smiling students seated in a row in a bright classroom">
  <div class="hero-card">
    <div class="tag">START IN</div>
    <div class="body">
      <h2>QUISQUE EGET TURPIS ID</h2>
      <p>Aenean sit nisi faucibus et urna rutrum, finibus fringilla massa. Lorem ipsum dolor sit amet, consectetur adipiscing elit.</p>
    </div>
    <span class="btn-pill">REGISTER ONLINE</span>
  </div>
</section>

<section class="events">
  <div class="sec-title" style="top:52px">
    <h2>Featured Events</h2>
    <span>View all events and join us</span>
    <svg width="90" height="14" viewBox="0 0 90 14"><line x1="0" y1="7" x2="38" y2="7" stroke="#6cc3a1"/><line x1="52" y1="7" x2="90" y2="7" stroke="#6cc3a1"/><path d="M40 2h10v10l-5-3-5 3z" fill="none" stroke="#6cc3a1"/></svg>
  </div>
  <article class="event" style="left:130px">
    <div class="date"><b>05</b><small>SEP</small></div>
    <div class="meta">7:00 pm - 9:00 pm &nbsp;|&nbsp; Nullam sit amet</div>
    <h3>Etiam imperdiet mauris lectus</h3>
    <div class="img" role="img" aria-label="Photo of students studying together around a laptop" style="background:linear-gradient(135deg,#8a6a4c,#d9b98e 50%,#6d5a48)"></div>
  </article>
  <article class="event" style="left:612px">
    <div class="date"><b>08</b><small>SEP</small></div>
    <div class="meta">7:00 pm - 9:00 pm &nbsp;|&nbsp; Nullam sit amet</div>
    <h3>Etiam imperdiet mauris lectus</h3>
    <div class="img" role="img" aria-label="Photo of a tutor presenting to students at a meeting table" style="background:linear-gradient(135deg,#c8ccd0,#8b98a6 50%,#5a6c7c)"></div>
  </article>
</section>

<section class="news">
  <div class="sec-title" style="top:56px">
    <h2>Latest News</h2>
    <span>From our blog</span>
    <svg width="90" height="14" viewBox="0 0 90 14"><line x1="0" y1="7" x2="38" y2="7" stroke="#6cc3a1"/><line x1="52" y1="7" x2="90" y2="7" stroke="#6cc3a1"/><path d="M40 2h10v10l-5-3-5 3z" fill="none" stroke="#6cc3a1"/></svg>
  </div>
  <article class="post" style="left:130px">
    <div class="img" role="img" aria-label="Photo of a group of smiling students" style="background:linear-gradient(135deg,#4a3a34,#9c7a66 60%,#d4c0ae)"></div>
    <div class="meta">Sep 05, 2016 &nbsp;/&nbsp; 3 comments</div>
    <h3>Quisque lobortis arcu in urna</h3>
    <p>Proin gravida nibh vel velit auctor aliquet. Aenean sollicitudin, lorem quis bibendum auctor, nisi elit consequat ipsum, nec sagittis sem nibh id elit.</p>
    <span class="more">READ MORE</span>
  </article>
  <article class="post" style="left:452px">
    <div class="img" role="img" aria-label="Photo of two students sitting outdoors with books" style="background:linear-gradient(135deg,#7b8f5a,#c2c79d 55%,#5d6e46)"></div>
    <div class="meta">Sep 05, 2016 &nbsp;/&nbsp; 3 comments</div>
    <h3>Quisque lobortis arcu in urna</h3>
    <p>Duis sed odio sit amet nibh vulputate cursus a sit amet mauris. Morbi accumsan ipsum velit. Nam nec tellus a odio tincidunt auctor a ornare odio. Sed non mauris vitae erat.</p>
    <span class="more">READ MORE</span>
  </article>
  <article class="post" style="left:773px">
    <div class="img" role="img" aria-label="Photo of students working at computers" style="background:linear-gradient(135deg,#5e6770,#b3b9bd 55%,#3c434a)"></div>
    <div class="meta">Sep 05, 2016 &nbsp;/&nbsp; 3 comments</div>
    <h3>Quisque lobortis arcu in urna</h3>
    <p>Proin gravida nibh vel velit auctor aliquet. Aenean sollicitudin, lorem quis bibendum auctor, nisi elit consequat ipsum, nec sagittis sem nibh id elit.</p>
    <span class="more">READ MORE</span>
  </article>
</section>

<section class="teachers">
  <div class="sec-title" style="top:56px">
    <h2>Our Teachers</h2>
    <span>We are professional</span>
    <svg width="90" height="14" viewBox="0 0 90 14"><line x1="0" y1="7" x2="38" y2="7" stroke="#6cc3a1"/><line x1="52" y1="7" x2="90" y2="7" stroke="#6cc3a1"/><path d="M40 2h10v10l-5-3-5 3z" fill="none" stroke="#6cc3a1"/></svg>
  </div>
  <div class="teacher" style="left:130px"><div class="img" role="img" aria-label="Portrait of a teacher at a chalkboard" style="background:linear-gradient(160deg,#4d5b4a,#a39a8a)"></div><h4>DONEC ELEMENTUM</h4><small>Head of Math</small></div>
  <div class="teacher" style="left:291px"><div class="img" role="img" aria-label="Portrait of a teacher in front of a blue board" style="background:linear-gradient(160deg,#2d6c8c,#8fb7c7)"></div><h4>DONEC ELEMENTUM</h4><small>Head of Arts</small></div>
  <div class="teacher" style="left:452px"><div class="img" role="img" aria-label="Portrait of a teacher in a suit" style="background:linear-gradient(160deg,#6c7580,#c8cbcf)"></div><h4>DONEC ELEMENTUM</h4><small>Head of Music</small></div>
  <div class="teacher" style="left:613px"><div class="img" role="img" aria-label="Portrait of a smiling teacher" style="background:linear-gradient(160deg,#a6b9b0,#e2cdbb)"></div><h4>DONEC ELEMENTUM</h4><small>Head of Science</small></div>
  <div class="teacher" style="left:774px"><div class="img" role="img" aria-label="Portrait of a senior teacher" style="background:linear-gradient(160deg,#7a8a7c,#d2c7b9)"></div><h4>DONEC ELEMENTUM</h4><small>Head of History</small></div>
  <div class="teacher" style="left:935px"><div class="img" role="img" aria-label="Portrait of a teacher beside a chalkboard" style="background:linear-gradient(160deg,#26506a,#a8b8c0)"></div><h4>DONEC ELEMENTUM</h4><small>Head of English</small></div>
</section>

<section class="courses">
  <div class="sec-title" style="top:52px">
    <h2>Popular Courses</h2>
    <span>We are professional</span>
    <svg width="90" height="14" viewBox="0 0 90 14"><line x1="0" y1="7" x2="38" y2="7" stroke="#6cc3a1"/><line x1="52" y1="7" x2="90" y2="7" stroke="#6cc3a1"/><path d="M40 2h10v10l-5-3-5 3z" fill="none" stroke="#6cc3a1"/></svg>
  </div>

  <div class="course" style="left:130px;top:172px;width:456px;height:425px">
    <div class="img" role="img" aria-label="Photo of students sharing a laptop outdoors" style="height:310px;background:linear-gradient(135deg,#5b6b3c,#b9a57c 55%,#7a5d3f)"></div>
    <div class="price" style="top:280px">FREE</div>
    <p style="top:352px">Aenean dignissim arcu in justo aliquet.</p>
    <h4 style="top:372px">Fusce orci lorem</h4>
  </div>

  <div class="course" style="left:612px;top:172px;width:217px;height:238px">
    <div class="img" role="img" aria-label="Photo of a tutor helping students" style="height:152px;background:linear-gradient(135deg,#3e4d62,#a78f73)"></div>
    <div class="price" style="top:122px">$50</div>
    <p style="top:192px">Aenean dignissim arcu in justo aliquet.</p>
    <h4 style="top:210px">Fusce orci lorem</h4>
  </div>
  <div class="course" style="left:853px;top:172px;width:217px;height:238px">
    <div class="img" role="img" aria-label="Photo of a teacher with cheering young students" style="height:152px;background:linear-gradient(135deg,#2f6b5a,#c9a070)"></div>
    <div class="price" style="top:122px">$50</div>
    <p style="top:192px">Aenean dignissim arcu in justo aliquet.</p>
    <h4 style="top:210px">Fusce orci lorem</h4>
  </div>

  <div class="course" style="left:612px;top:435px;width:458px;height:425px">
    <div class="img" role="img" aria-label="Overhead photo of students working on a bench" style="height:310px;background:linear-gradient(135deg,#9c9d9a,#d8d6d0 50%,#b98f3f)"></div>
    <div class="price" style="top:280px">FREE</div>
    <p style="top:352px">Aenean dignissim arcu in justo aliquet.</p>
    <h4 style="top:372px">Fusce orci lorem</h4>
  </div>

  <div class="course" style="left:130px;top:622px;width:217px;height:238px">
    <div class="img" role="img" aria-label="Photo of a teacher with students at a whiteboard" style="height:152px;background:linear-gradient(135deg,#c9cfd2,#5f7a8a)"></div>
    <div class="price" style="top:122px">$50</div>
    <p style="top:192px">Aenean dignissim arcu in justo aliquet.</p>
    <h4 style="top:210px">Fusce orci lorem</h4>
  </div>
  <div class="course" style="left:373px;top:622px;width:213px;height:238px">
    <div class="img" role="img" aria-label="Photo of a student reading" style="height:152px;background:linear-gradient(135deg,#d6d1c8,#8f8779)"></div>
    <div class="price" style="top:122px">$50</div>
    <p style="top:192px">Aenean dignissim arcu in justo aliquet.</p>
    <h4 style="top:210px">Fusce orci lorem</h4>
  </div>

  <div class="view-all">VIEW ALL COURSES</div>
</section>

<section class="cta">
  <h2>PRAESENT QUIS RISUS MALESUADA, PRETIUM ORCI NON</h2>
  <p>PRAESENT QUIS RISUS MALESUADA, PRETIUM ORCI NON, PRETIUM NEQUE</p>
  <span class="btn">CONTACT US TODAY &nbsp;›</span>
</section>

<footer class="footer">
  <div class="fcol" style="left:130px">
    <h5>Newsletter</h5>
    <p>Proin gravida nibh vel velit auctor aliquet. Aenean sollicitudin, lorem quis bibendum auctor nisi elit consequat.</p>
    <div class="email"><span>YOUR EMAIL</span><span>›</span></div>
  </div>
  <div class="fcol" style="left:371px">
    <h5>Recent Post</h5>
    <div class="fpost"><b>Etiam malesuada magna</b><small>Sep 05, 2016 / 3 comments</small></div>
    <div class="fpost"><b>Etiam volutpat nec odio id sollicitudin</b><small>Sep 05, 2016 / 3 comments</small></div>
  </div>
  <div class="fcol" style="left:612px">
    <h5>Quick Link</h5>
    <ul class="flinks"><li>Tutor Registration</li><li>Parent Registration</li><li>Tutor Profile</li><li>Calendar</li><li>Event</li><li>Our Courses</li></ul>
  </div>
  <div class="fcol" style="left:852px">
    <h5>Contact Info</h5>
    <p>No 1125, Aenean elit mi, faucibus et urna rutrum, finibus fringilla Massa</p>
    <div class="contact-line">+00 123 456 78 99</div>
    <p>hello@brightlane.example</p>
    <div class="fsocial"><i></i><i></i><i></i><i></i></div>
  </div>
</footer>
<div class="copyright">© 2016 Brightlane Tutoring. All rights reserved.</div>

</body>
</html>
```